Selva Ola Verde Adventure Vacation Rack Card

We need a double sided rack card design. One side should be promoting our "Days Of Roaming" tour with the flip side promoting our "Honeymoon" and "Custom & Family Tours". Colours should be in line with our website www.SelvaOlaVerde.com. Text and photos attached (feel free to use as necessary). We are looking for a fun rack card that will catch clients eyes and hopefully promote Costa Rica as a fun and exciting vacation.

Target Market(s)

Tourism - USA and Canada

Industry/Entity Type

Tourism

Font styles to use
Sans Serif

Colors
0455a3
33a6d7
f37122

Requirements
Must have
• Our logo on both sides of the rack card. Must be bright and fun looking. Costa Rica is an outdoor destination with tons of fun activities to do, we want to try and get that feeling across on the card.
Nice to have
• I have added a price sticker to the attachments on this project. Is it possible to have something similar on the Days of Roaming side? The price would be $1999 scored out with the new price being $1649.

```html
<!DOCTYPE html>
<html lang="en">
<head>
<meta charset="utf-8">
<title>Selva Ola Verde Rack Card</title>
<link rel="stylesheet" href="https://fonts.googleapis.com/css2?family=Archivo+Black&family=Open+Sans:wght@400;700;800&family=Shadows+Into+Light&display=swap">
<style>
  :root {
    --orange: #f7941d;
    --orange-deep: #f37122;
    --blue: #0455a3;
    --headline-blue: #1d3fd6;
    --sky: #33a6d7;
    --cyan-box: #8ff0fb;
    --red: #a5161c;
    --sticker-red: #c8141e;
    --gold: #f6d12b;
    --white: #ffffff;
    --page: #ece8e2;
  }
  * { box-sizing: border-box; margin: 0; padding: 0; }
  html, body { width: 988px; height: 1200px; overflow: hidden; }
  body { background: var(--page); font-family: "Open Sans", Arial, sans-serif; position: relative; }

  .rack-card {
    position: absolute; width: 420px; height: 800px;
    background: var(--white); overflow: hidden;
    box-shadow: 0 6px 18px rgba(0,0,0,.25);
  }
  .rack-card--front { left: 50px; top: 40px; }
  .rack-card--back { left: 518px; top: 360px; }

  .card-bg { position: absolute; inset: 0; width: 100%; height: 100%; }

  .brand { position: absolute; top: 44px; left: 0; width: 100%; display: flex; align-items: center; justify-content: center; gap: 12px; }
  .brand__name { font-family: "Open Sans", Arial, sans-serif; font-weight: 400; font-size: 36px; color: var(--orange-deep); letter-spacing: 1px; text-transform: uppercase; line-height: 1; }
  .brand__dot { width: 30px; height: 30px; border-radius: 50%; background: var(--sky); }

  .photo { position: absolute; border: 4px solid var(--cyan-box); }

  .price-sticker {
    position: absolute; left: 52px; top: 240px; width: 92px; height: 92px; border-radius: 50%;
    background: var(--sticker-red); border: 4px solid var(--gold);
    display: flex; flex-direction: column; align-items: center; justify-content: center;
    color: var(--white); font-weight: 800; line-height: 1.1;
  }
  .price-sticker__old { font-size: 15px; text-decoration: line-through; opacity: .9; }
  .price-sticker__new { font-size: 19px; }

  .headline { position: absolute; font-family: "Archivo Black", Arial, sans-serif; color: var(--headline-blue); text-transform: uppercase; line-height: 1.05; }
  .headline--tour { left: 160px; top: 272px; font-size: 25px; }
  .headline--custom { left: 24px; top: 205px; font-size: 20px; }

  .tagline { position: absolute; color: var(--red); font-weight: 800; font-size: 17px; }
  .tagline--tour { left: 56px; top: 344px; }
  .tagline--custom { right: 30px; top: 270px; }

  .itinerary { position: absolute; left: 62px; top: 374px; width: 300px; color: var(--white); font-weight: 700; font-size: 10.5px; line-height: 16.5px; list-style: none; }

  .script-note { position: absolute; left: 118px; top: 576px; width: 250px; font-family: "Shadows Into Light", cursive; color: var(--headline-blue); font-size: 16px; line-height: 1.15; }

  .surfboards { position: absolute; left: 0; top: 620px; width: 420px; height: 180px; clip-path: polygon(0 0, 100% 70%, 100% 100%, 0 100%); background: linear-gradient(90deg,#e9d9b8,#c9542a 25%,#f1e7d0 45%,#3b6ea5 65%,#e5c04a 85%,#8a3b2a); }

  .toucan { position: absolute; left: 300px; top: 625px; width: 86px; height: 86px; border-radius: 50%; border: 4px solid var(--blue); background: radial-gradient(circle at 45% 40%, #f4c430, #1a1a1a 70%); }

  .contact { position: absolute; background: var(--cyan-box); border: 2px solid var(--white); border-radius: 6px; padding: 8px 12px; color: var(--blue); font-size: 12.5px; line-height: 17px; font-style: normal; }
  .contact--front { left: 108px; top: 700px; width: 272px; }
  .contact--back { left: 50px; top: 684px; width: 272px; }

  .about { position: absolute; left: 70px; top: 290px; width: 290px; text-align: center; color: var(--white); font-weight: 700; font-size: 11px; line-height: 18px; }
  .about p + p { margin-top: 14px; }
  .signoff { position: absolute; right: 88px; top: 500px; font-family: "Shadows Into Light", cursive; color: var(--red); font-size: 14px; }

  .frog { position: absolute; left: 262px; top: 118px; width: 120px; height: 92px; border-radius: 46% 46% 40% 40%; background: radial-gradient(circle at 50% 45%, #7fd13b, #2f8a2a 70%); }
</style>
</head>
<body>

<!-- Front: tour side -->
<section class="rack-card rack-card--front">
  <svg class="card-bg" viewBox="0 0 420 800" preserveAspectRatio="none" aria-hidden="true">
    <path d="M0 190 Q150 200 420 330 L420 800 L0 800 Z" fill="var(--orange)"/>
    <path d="M0 160 Q160 170 420 250 L420 300 Q180 200 0 190 Z" fill="#d6f3fb"/>
  </svg>

  <div class="brand"><span class="brand__name">Selva Ola Verde</span><span class="brand__dot"></span></div>

  <div class="photo" role="img" aria-label="Photo of a garden pool in the jungle" style="left:8px;top:172px;width:122px;height:100px;background:linear-gradient(160deg,#4e8a3a,#2d5a2a 60%,#6f9f5a);"></div>
  <div class="photo" role="img" aria-label="Photo of a canyoning adventurer at a waterfall" style="left:134px;top:168px;width:122px;height:102px;background:linear-gradient(160deg,#3c4a3a,#7a8870 60%,#cfd6c4);"></div>
  <div class="photo" role="img" aria-label="Photo of a whitewater rafting crew" style="left:262px;top:158px;width:136px;height:98px;background:linear-gradient(160deg,#2f3a2e,#5b7b9a 60%,#d9e8f2);"></div>

  <div class="price-sticker">
    <span class="price-sticker__old">$1999</span>
    <span class="price-sticker__new">$1649</span>
  </div>

  <h1 class="headline headline--tour">Days of<br>Roaming</h1>

  <h2 class="tagline tagline--tour">8 Days, 8 Adventures, 1 Life</h2>

  <ul class="itinerary">
    <li>Itinerary:</li>
    <li>Day 1 – Pick Up San Jose International Airport</li>
    <li>Day 2 – Beginner Kayaking</li>
    <li>Day 3 – Whitewater Rafting. Overnight Jungle Lodge</li>
    <li>Day 4 – Canopy/Zipline Tour &amp; Jungle Hikes. Overnight Jungle Lodge</li>
    <li>Day 5 – Whitewater Rafting &amp; Beach</li>
    <li>Day 6 – Surfing &amp; Snorkeling</li>
    <li>Day 7 – Canyoning (Rappelling Waterfalls) or Mountain Biking. Your choice!</li>
    <li>Day 8 – Drop Off San Jose International Airport</li>
  </ul>

  <p class="script-note">Come join us in the tropics on one of our all inclusive 8 day week of Adventure tours.</p>

  <div class="surfboards" role="img" aria-label="Photo of colourful surfboards standing in a row"></div>

  <div class="toucan" role="img" aria-label="Photo of a toucan"></div>

  <address class="contact contact--front">
    Email: info@SelvaOlaVerde.com<br>
    Tel: 1-888-555-0142<br>
    Website: www.SelvaOlaVerde.com
  </address>
</section>

<!-- Back: honeymoon and custom tours side -->
<section class="rack-card rack-card--back">
  <svg class="card-bg" viewBox="0 0 420 800" preserveAspectRatio="none" aria-hidden="true">
    <path d="M0 250 Q200 190 420 130 L420 800 L0 800 Z" fill="var(--orange)"/>
    <path d="M0 225 Q120 190 230 165 L230 180 Q120 205 0 250 Z" fill="#d6f3fb"/>
    <path d="M0 560 Q220 540 420 500 L420 520 Q220 560 0 580 Z" fill="var(--white)"/>
    <path d="M0 640 Q220 660 420 628 L420 800 L0 800 Z" fill="#8fd3e0"/>
  </svg>

  <div class="brand"><span class="brand__name">Selva Ola Verde</span><span class="brand__dot"></span></div>

  <div class="frog" role="img" aria-label="Illustration of a red-eyed tree frog"></div>

  <h1 class="headline headline--custom">Honeymoon /<br>Custom &amp; Family Tours</h1>

  <h2 class="tagline tagline--custom">100% Adventure</h2>

  <div class="about">
    <p>Selva Ola Verde has been specializing in helping plan unique tropical getaways since 1995. Based in Costa Rica 365 days a year, we are able to recommend the best activities, hotels and destinations to suit your vacation/honeymoon desires.</p>
    <p>We have personally explored and enjoyed many of the region's attractions and know which ones will give you the best experience while you are here. Let us know what you are looking for and we'll come up with an incredible itinerary, just for you!</p>
  </div>
  <span class="signoff">xoxo</span>

  <div class="photo" role="img" aria-label="Photo of a couple walking on a beach" style="left:6px;top:540px;width:122px;height:92px;background:linear-gradient(170deg,#7fb6cf,#e7e2d2 60%,#c9b999);"></div>
  <div class="photo" role="img" aria-label="Photo of a lit cave pool" style="left:134px;top:552px;width:122px;height:96px;background:radial-gradient(circle at 50% 60%,#d07a2e,#3a2416 70%);"></div>
  <div class="photo" role="img" aria-label="Photo of feet in the sand by the sea" style="left:262px;top:528px;width:140px;height:90px;background:linear-gradient(170deg,#5fc7d6,#e8d2b8 55%,#c98f6e);"></div>

  <address class="contact contact--back">
    Email: info@SelvaOlaVerde.com<br>
    Tel: 1-888-555-0142<br>
    Website: www.SelvaOlaVerde.com
  </address>
</section>

</body>
</html>
```